Letterhead Design for Law Firm that Specializes in Property Damage Litigation

We are looking for a redesign of our letterhead. Our current letterhead lists all of our current staff members and we'd like to come up with a design that does NOT list all of the staff members so that it does not need to be updated with every newly hired employee. Must be in editable format.

We are a law firm that specializes in property damage, so we need something that is professional, yet modern. The final design should use our existing logo and should use a blue color scheme (alternate colors would be gray, black, and white).

Industry/Entity Type

Legal

Colors
0054AA
0677BA
7BADD7
CADEEF
E8F1F8

```html
<!DOCTYPE html>
<html lang="en">
<head>
<meta charset="utf-8">
<title>Hartwell Monroe &amp; Castell — Letterhead</title>
<link rel="stylesheet" href="https://fonts.googleapis.com/css2?family=Cinzel:wght@500&family=Source+Sans+3:wght@400;600;700&display=swap">
<style>
  :root {
    --navy: #1b335f;
    --slate: #5e5e5e;
    --ink: #555555;
    --paper: #f4f4f4;
    --backdrop: #e3e3e3;
    --rule: #4a4a4a;
    --white: #ffffff;
  }
  * { margin: 0; padding: 0; box-sizing: border-box; }
  html, body { width: 1200px; height: 1200px; overflow: hidden; }
  body {
    background: var(--backdrop);
    font-family: "Source Sans 3", Arial, sans-serif;
    position: relative;
  }
  .letterhead {
    position: absolute;
    left: 167px; top: 40px;
    width: 866px; height: 1120px;
    background: var(--paper);
  }
  .brand-square {
    position: absolute;
    left: 71px; top: 78px;
    width: 62px; height: 62px;
    background: var(--slate);
  }
  .firm-name {
    position: absolute;
    left: 186px; top: 68px;
    font-family: "Cinzel", "Times New Roman", serif;
    font-weight: 500;
    font-size: 31px;
    line-height: 30px;
    color: var(--navy);
    letter-spacing: 0.5px;
  }
  .tagline {
    position: absolute;
    left: 71px; top: 168px;
    font-size: 12.5px;
    font-weight: 600;
    letter-spacing: 2.6px;
    color: var(--slate);
    text-transform: uppercase;
  }
  .divider {
    position: absolute;
    left: 423px; top: 0;
    width: 1.5px; height: 184px;
    background: var(--rule);
  }
  .office {
    position: absolute;
    top: 71px;
    font-size: 12px;
    line-height: 15.5px;
    color: var(--ink);
  }
  .office--pa { left: 461px; }
  .office--nj { left: 659px; }
  .office h2 {
    font-family: "Cinzel", "Times New Roman", serif;
    font-weight: 500;
    font-size: 14px;
    color: var(--navy);
    letter-spacing: 0.3px;
    line-height: 17px;
    margin-bottom: 0;
  }
  .office address { font-style: normal; }
  .office .lines { margin-top: 6px; }
  .office .line { display: flex; align-items: center; gap: 3px; }
  .office .line svg { width: 11px; height: 11px; fill: var(--navy); }
  .footer-band {
    position: absolute;
    left: 0; bottom: 0;
    width: 100%; height: 41px;
    background: var(--navy);
  }
  .footer-band .web {
    position: absolute;
    left: 71px; top: 11px;
    color: var(--white);
    font-weight: 700;
    font-size: 13.5px;
    letter-spacing: 1.6px;
  }
</style>
</head>
<body>
  <main class="letterhead">
    <div class="brand-square"></div>
    <h1 class="firm-name">HARTWELL<br>MONROE &amp;<br>CASTELL</h1>
    <p class="tagline">The Property Damage Attorneys</p>

    <div class="divider"></div>

    <section class="office office--pa">
      <h2>PHILADELPHIA OFFICE</h2>
      <address>2240 Market Crossing<br>Suite 1480<br>Philadelphia, PA 19103</address>
      <div class="lines">
        <div class="line"><svg viewBox="0 0 24 24"><path d="M6.6 10.8a15.1 15.1 0 0 0 6.6 6.6l2.2-2.2c.3-.3.7-.4 1-.2 1.1.4 2.3.6 3.6.6.6 0 1 .4 1 1V20c0 .6-.4 1-1 1C10.6 21 3 13.4 3 4c0-.6.4-1 1-1h3.5c.6 0 1 .4 1 1 0 1.2.2 2.4.6 3.6.1.3 0 .7-.2 1z"/></svg>215.555.0142</div>
        <div class="line"><svg viewBox="0 0 24 24"><path d="M6 2h10l2 2v5H6zM3 10h18c1 0 2 1 2 2v8H1v-8c0-1 1-2 2-2zm3 6v6h12v-6z"/></svg>215.555.0178</div>
      </div>
    </section>

    <section class="office office--nj">
      <h2>NEW JERSEY OFFICE</h2>
      <address>725 Laurel Avenue East<br>Suite 205<br>Cherry Hill, NJ 08034</address>
      <div class="lines">
        <div class="line"><svg viewBox="0 0 24 24"><path d="M6.6 10.8a15.1 15.1 0 0 0 6.6 6.6l2.2-2.2c.3-.3.7-.4 1-.2 1.1.4 2.3.6 3.6.6.6 0 1 .4 1 1V20c0 .6-.4 1-1 1C10.6 21 3 13.4 3 4c0-.6.4-1 1-1h3.5c.6 0 1 .4 1 1 0 1.2.2 2.4.6 3.6.1.3 0 .7-.2 1z"/></svg>856.555.0163</div>
        <div class="line"><svg viewBox="0 0 24 24"><path d="M6 2h10l2 2v5H6zM3 10h18c1 0 2 1 2 2v8H1v-8c0-1 1-2 2-2zm3 6v6h12v-6z"/></svg>215.555.0178</div>
      </div>
    </section>

    <footer class="footer-band">
      <span class="web">www.hmclegal.com</span>
    </footer>
  </main>
</body>
</html>
```